Business cards for law firm with global theme

I'd like business cards with contact info for two offices. They should include the colors and font of the new logo design, which is a stylized globe with an "F" in it. The feel should be very modern and professional.

```html
<!DOCTYPE html>
<html lang="en">
<head>
<meta charset="UTF-8">
<title>Varenna Law – Business Cards</title>
<link rel="stylesheet" href="https://fonts.googleapis.com/css2?family=Montserrat:wght@600;700&family=Arimo:wght@400;700&display=swap">
<style>
  :root {
    --page-bg: #d9dadc;
    --card-white: #f7f7f7;
    --navy: #0b3466;
    --bright-blue: #1a9ad6;
    --back-navy: #0a3c70;
    --back-mark: #0e4d8f;
    --text-grey: #3c3f44;
    --divider: #d3d5d8;
  }
  * { margin: 0; padding: 0; box-sizing: border-box; }
  html, body { width: 1200px; height: 800px; overflow: hidden; }
  body {
    background: var(--page-bg);
    display: flex;
    align-items: center;
    justify-content: center;
    gap: 48px;
    font-family: "Arimo", Arial, sans-serif;
  }
  .card {
    width: 540px;
    height: 310px;
    border-radius: 24px;
    position: relative;
    overflow: hidden;
    box-shadow: 0 10px 26px rgba(0,0,0,0.18);
  }
  .card-front {
    background: var(--card-white);
    display: flex;
    border-bottom: 4px solid var(--bright-blue);
  }
  .brand-panel {
    width: 270px;
    flex: none;
    padding: 0 24px;
    display: flex;
    flex-direction: column;
    align-items: center;
    justify-content: center;
    gap: 14px;
  }
  .brand-lockup { display: flex; align-items: center; gap: 10px; white-space: nowrap; }
  .brand-dot {
    width: 26px; height: 26px; border-radius: 50%; flex: none;
    background: var(--bright-blue);
  }
  .brand-name {
    font-family: "Montserrat", Arial, sans-serif;
    font-weight: 700;
    font-size: 22px;
    letter-spacing: 1px;
    color: var(--navy);
    text-transform: uppercase;
    line-height: 1.1;
  }
  .brand-rule { width: 200px; height: 2px; background: var(--bright-blue); }
  .panel-divider { width: 1px; flex: none; margin: 36px 0; background: var(--divider); }
  .contact-panel {
    flex: 1;
    padding: 34px 20px 0 24px;
    color: var(--text-grey);
    font-size: 12px;
    line-height: 1.4;
  }
  .person-name {
    font-family: "Montserrat", Arial, sans-serif;
    font-weight: 700;
    font-size: 18px;
    color: var(--navy);
    line-height: 1.2;
  }
  .person-title { font-size: 12px; margin-bottom: 7px; }
  .offices { display: flex; gap: 14px; margin-bottom: 8px; }
  .office-label { font-weight: 700; color: var(--navy); font-size: 11px; text-transform: uppercase; letter-spacing: 0.5px; }
  .contact-list { list-style: none; }
  .contact-list li { display: flex; align-items: center; gap: 8px; }
  .contact-list svg { width: 12px; height: 12px; flex: none; fill: var(--bright-blue); }
  .card-back {
    background: var(--back-navy);
    display: flex;
    flex-direction: column;
    align-items: center;
    justify-content: center;
    gap: 16px;
    border-bottom: 4px solid var(--bright-blue);
  }
  .card-back .brand-dot { background: var(--back-mark); width: 40px; height: 40px; }
  .card-back .brand-name { color: var(--back-mark); font-size: 40px; }
  .card-back .brand-rule { width: 280px; background: var(--back-mark); }
</style>
</head>
<body>
  <section class="card card-front">
    <div class="brand-panel">
      <div class="brand-lockup">
        <span class="brand-dot"></span>
        <span class="brand-name">Varenna Law</span>
      </div>
      <span class="brand-rule"></span>
    </div>
    <div class="panel-divider"></div>
    <div class="contact-panel">
      <p class="person-name">Daniel Marsh</p>
      <p class="person-title">Managing Director</p>
      <div class="offices">
        <p class="address"><span class="office-label">Juneau</span><br>1420 Harbor View Road<br>Juneau, Alaska 99801</p>
        <p class="address"><span class="office-label">Anchorage</span><br>88 Glacier Avenue<br>Anchorage, Alaska 99501</p>
      </div>
      <ul class="contact-list">
        <li><svg viewBox="0 0 12 12"><path d="M2.5 1h2l1 2.6-1.3 1a6 6 0 0 0 2.7 2.7l1-1.3L11 7v2a1.5 1.5 0 0 1-1.6 1.5A9 9 0 0 1 1 2.6 1.5 1.5 0 0 1 2.5 1z"/></svg>555-210-4471</li>
        <li><svg viewBox="0 0 12 12"><path d="M3.5 0h5A1 1 0 0 1 9.5 1v10a1 1 0 0 1-1 1h-5a1 1 0 0 1-1-1V1a1 1 0 0 1 1-1zM4 1.5v8h4v-8zM6 10.2a.6.6 0 1 0 0 1.2.6.6 0 0 0 0-1.2z"/></svg>555-318-2096</li>
        <li><svg viewBox="0 0 12 12"><path d="M3 0h5v3H3zM1 4h10v6H9v2H3v-2H1zM4 8v3h4V8z"/></svg>555-427-6630</li>
        <li><svg viewBox="0 0 12 12"><path d="M0 2h12v8H0zM1 3v.4l5 3.3 5-3.3V3z"/></svg>info@varennalaw.com</li>
        <li><svg viewBox="0 0 12 12"><path d="M6 0a6 6 0 1 0 0 12A6 6 0 0 0 6 0zm0 1.2c.7 0 1.5 1.6 1.7 4.2H4.3C4.5 2.8 5.3 1.2 6 1.2zM1.3 6.6h2c.1 1.6.4 3 .9 3.9A4.8 4.8 0 0 1 1.3 6.6zm0-1.2a4.8 4.8 0 0 1 2.9-3.9c-.5.9-.8 2.300-.9 3.9zm3 1.2h3.4C7.5 9.2 6.7 10.8 6 10.8S4.5 9.2 4.3 6.6zm4.4 0h2a4.8 4.8 0 0 1-2.9 3.9c.5-.9.8-2.3.9-3.9zm0-1.2c-.1-1.6-.4-3-.9-3.9a4.8 4.8 0 0 1 2.9 3.9z"/></svg>www.varennalaw.com</li>
      </ul>
    </div>
  </section>

  <section class="card card-back">
    <div class="brand-lockup">
      <span class="brand-dot"></span>
      <span class="brand-name">Varenna Law</span>
    </div>
    <span class="brand-rule"></span>
  </section>
</body>
</html>
```